Design einer Auto-Folie für KR-Van
Zielgruppe
Privat - Autofolie für KR Van 6.1 Camper Heckklappe entwerfen - eher handwerklich statt kreativ
Aufgabenstellung
* Maße 139 cm x 9,5 cm - Bitte unten genannte Flaggen einbauen
* Muster unten mit falschen Flaggen - müssen richtig ausgewählt und in Grösse angepasst werden.: See Draft_Design01.pdf
* Reihenfolge von links
* EU - DE - A - IT - CH - NL - ES - F - POR - visiting friends - KELMOR - UK - IRL - BEL - DAN - NOR - S - FIN -POL - CZ - GRI - BAYERN
* Kelmor Rad - auswählen, welches am besten farblich passt
* Flaggen selber besorgen
* Maße Folie für Autotür (Heckklappe KR Van Tramo 6.1): 139 cm x 9,5 cm
* Einbauort siehe Foto KR Tramo Weis Heckklappe unten - unter Falz
=> Endprodukt: Druckvorlage für Foliendruck erstellen

```html
<!DOCTYPE html>
<html lang="de">
<head>
<meta charset="utf-8">
<title>KR-Van Heckklappen-Folie – Flaggenband</title>
<link rel="stylesheet" href="https://fonts.googleapis.com/css2?family=PT+Sans+Narrow:wght@700&display=swap">
<style>
  :root {
    --page: #ffffff;
    --eu-blue: #2f3a8f;
    --star-yellow: #f5d20a;
    --black: #1b1b1b;
    --red: #d8232f;
    --gold: #f5cf12;
    --white: #ffffff;
    --uk-blue: #2a3c7e;
    --green: #169b45;
    --nl-blue: #2f3f8c;
    --es-yellow: #f3bd18;
    --fr-blue: #2e3c8e;
    --pt-green: #0f7a33;
    --ua-blue: #4a6fc0;
    --ua-yellow: #f4d81e;
    --ie-orange: #ef8436;
    --nordic-blue: #2f5fa8;
    --fi-blue: #243f8a;
    --pl-red: #dc2f45;
    --cz-blue: #2c3f88;
    --gr-blue: #1e5fb4;
    --bavaria-blue: #5d9fdc;
    --bavaria-light: #dcecf8;
    --badge-gold: #e0b321;
    --badge-dark: #3a3a3a;
    --strip-bg: #eeeeee;
  }
  html, body {
    margin: 0;
    padding: 0;
    width: 1200px;
    height: 1169px;
    overflow: hidden;
    background: var(--page);
  }
  .foil-strip {
    position: absolute;
    left: 0;
    top: 541px;
    width: 1200px;
    height: 86px;
    display: block;
  }
  .motto {
    font-family: "PT Sans Narrow", "Arial Narrow", sans-serif;
    font-weight: 700;
    font-size: 24px;
    fill: var(--gold);
  }
  .club-name {
    font-family: "PT Sans Narrow", "Arial Narrow", sans-serif;
    font-weight: 700;
    font-size: 19px;
    fill: var(--badge-dark);
  }
</style>
</head>
<body>
<svg class="foil-strip" viewBox="0 0 1955 140" preserveAspectRatio="none" xmlns="http://www.w3.org/2000/svg" xmlns:xlink="http://www.w3.org/1999/xlink" aria-label="Flaggenband für die Heckklappe, 139 x 9,5 cm">
  <defs>
    <polygon id="star" points="0,-6 1.4,-1.9 5.7,-1.9 2.2,0.7 3.5,4.9 0,2.4 -3.5,4.9 -2.2,0.7 -5.7,-1.9 -1.4,-1.9" fill="var(--star-yellow)"/>
    <clipPath id="clip-uk"><rect x="275" y="6" width="106" height="99"/></clipPath>
    <clipPath id="clip-reflection"><rect x="0" y="105" width="1955" height="35"/></clipPath>
    <linearGradient id="fade" x1="0" y1="0" x2="0" y2="1">
      <stop offset="0" stop-color="#fff" stop-opacity="0.45"/>
      <stop offset="1" stop-color="#fff" stop-opacity="0.85"/>
    </linearGradient>
    <linearGradient id="bavaria-tone" x1="0" y1="0" x2="1" y2="1">
      <stop offset="0" stop-color="var(--bavaria-blue)"/>
      <stop offset="0.5" stop-color="var(--bavaria-light)"/>
      <stop offset="1" stop-color="var(--bavaria-blue)"/>
    </linearGradient>
    <linearGradient id="center-tone" x1="0" y1="0" x2="1" y2="1">
      <stop offset="0" stop-color="#b9d6ee"/>
      <stop offset="0.5" stop-color="#e6f1fa"/>
      <stop offset="1" stop-color="#b9d6ee"/>
    </linearGradient>
  </defs>

  <rect class="strip-background" x="0" y="0" width="1955" height="140" fill="var(--strip-bg)"/>

  <g id="flags">
    <!-- EU -->
    <g class="flag flag-eu">
      <rect x="8" y="6" width="138" height="99" fill="var(--eu-blue)"/>
      <use href="#star" x="77" y="22"/><use href="#star" x="93.5" y="26.4"/><use href="#star" x="105.6" y="38.5"/>
      <use href="#star" x="110" y="55"/><use href="#star" x="105.6" y="71.5"/><use href="#star" x="93.5" y="83.6"/>
      <use href="#star" x="77" y="88"/><use href="#star" x="60.5" y="83.6"/><use href="#star" x="48.4" y="71.5"/>
      <use href="#star" x="44" y="55"/><use href="#star" x="48.4" y="38.5"/><use href="#star" x="60.5" y="26.4"/>
    </g>
    <!-- DE -->
    <g class="flag flag-de">
      <rect x="150" y="6" width="120" height="33" fill="var(--black)"/>
      <rect x="150" y="39" width="120" height="33" fill="var(--red)"/>
      <rect x="150" y="72" width="120" height="33" fill="var(--gold)"/>
    </g>
    <!-- UK -->
    <g class="flag flag-uk" clip-path="url(#clip-uk)">
      <rect x="275" y="6" width="106" height="99" fill="var(--uk-blue)"/>
      <path d="M275 6 L381 105 M381 6 L275 105" stroke="var(--white)" stroke-width="18"/>
      <path d="M275 6 L381 105 M381 6 L275 105" stroke="var(--red)" stroke-width="6"/>
      <path d="M328 6 V105 M275 55.5 H381" stroke="var(--white)" stroke-width="24"/>
      <path d="M328 6 V105 M275 55.5 H381" stroke="var(--red)" stroke-width="14"/>
    </g>
    <!-- AT -->
    <g class="flag flag-at">
      <rect x="384" y="6" width="93" height="33" fill="var(--red)"/>
      <rect x="384" y="39" width="93" height="33" fill="var(--white)"/>
      <rect x="384" y="72" width="93" height="33" fill="var(--red)"/>
    </g>
    <!-- IT -->
    <g class="flag flag-it">
      <rect x="480" y="6" width="20" height="99" fill="var(--green)"/>
      <rect x="500" y="6" width="17" height="99" fill="var(--white)"/>
      <rect x="517" y="6" width="18" height="99" fill="var(--red)"/>
    </g>
    <!-- CH -->
    <g class="flag flag-ch">
      <rect x="535" y="6" width="102" height="99" fill="var(--red)"/>
      <rect x="563" y="6" width="74" height="99" fill="var(--red)" stroke="var(--white)" stroke-width="0"/>
      <rect x="594" y="32" width="14" height="46" fill="var(--white)"/>
      <rect x="578" y="48" width="46" height="14" fill="var(--white)"/>
    </g>
    <!-- NL -->
    <g class="flag flag-nl">
      <rect x="640" y="6" width="66" height="33" fill="var(--red)"/>
      <rect x="640" y="39" width="66" height="33" fill="var(--white)"/>
      <rect x="640" y="72" width="66" height="33" fill="var(--nl-blue)"/>
    </g>
    <!-- ES -->
    <g class="flag flag-es">
      <rect x="708" y="6" width="60" height="25" fill="var(--red)"/>
      <rect x="708" y="31" width="60" height="49" fill="var(--es-yellow)"/>
      <rect x="708" y="80" width="60" height="25" fill="var(--red)"/>
    </g>
    <!-- FR -->
    <g class="flag flag-fr">
      <rect x="770" y="6" width="18" height="99" fill="var(--fr-blue)"/>
      <rect x="788" y="6" width="18" height="99" fill="var(--white)"/>
    </g>
    <!-- PT -->
    <g class="flag flag-pt">
      <rect x="806" y="6" width="27" height="99" fill="var(--pt-green)"/>
      <rect x="833" y="6" width="42" height="99" fill="var(--red)"/>
      <circle cx="834" cy="52" r="10" fill="var(--es-yellow)"/>
    </g>

    <!-- Center: visiting friends + club -->
    <g class="center-panel">
      <rect x="878" y="0" width="199" height="140" fill="url(#center-tone)" role="img" aria-label="Bayerisches Rautenmuster in Hellblau und Weiß als Hintergrund"/>
      <text class="motto" x="977.5" y="24" text-anchor="middle">VISITING FRIENDS</text>
      <circle cx="977.5" cy="82" r="42" fill="var(--badge-gold)"/>
      <text class="club-name" x="977.5" y="89" text-anchor="middle">KELMOR</text>
    </g>

    <!-- UA -->
    <g class="flag flag-ua">
      <rect x="1080" y="6" width="45" height="50" fill="var(--ua-blue)"/>
      <rect x="1080" y="56" width="45" height="49" fill="var(--ua-yellow)"/>
    </g>
    <!-- IE -->
    <g class="flag flag-ie">
      <rect x="1125" y="6" width="15" height="99" fill="var(--green)"/>
      <rect x="1140" y="6" width="17" height="99" fill="var(--white)"/>
      <rect x="1157" y="6" width="13" height="99" fill="var(--ie-orange)"/>
    </g>
    <!-- BE -->
    <g class="flag flag-be">
      <rect x="1170" y="6" width="19" height="99" fill="var(--black)"/>
      <rect x="1189" y="6" width="20" height="99" fill="var(--gold)"/>
      <rect x="1209" y="6" width="19" height="99" fill="var(--red)"/>
    </g>
    <!-- DK -->
    <g class="flag flag-dk">
      <rect x="1230" y="6" width="58" height="99" fill="var(--red)"/>
      <rect x="1252" y="6" width="12" height="99" fill="var(--white)"/>
      <rect x="1230" y="49" width="58" height="12" fill="var(--white)"/>
    </g>
    <!-- NI -->
    <g class="flag flag-ni">
      <rect x="1290" y="6" width="65" height="99" fill="var(--white)"/>
      <rect x="1317" y="6" width="11" height="99" fill="var(--red)"/>
      <rect x="1290" y="50" width="65" height="11" fill="var(--red)"/>
    </g>
    <!-- SE -->
    <g class="flag flag-se">
      <rect x="1357" y="6" width="71" height="99" fill="var(--nordic-blue)"/>
      <rect x="1380" y="6" width="13" height="99" fill="var(--gold)"/>
      <rect x="1357" y="49" width="71" height="13" fill="var(--gold)"/>
    </g>
    <!-- FI -->
    <g class="flag flag-fi">
      <rect x="1430" y="6" width="78" height="99" fill="var(--white)"/>
      <rect x="1455" y="6" width="14" height="99" fill="var(--fi-blue)"/>
      <rect x="1430" y="48" width="78" height="14" fill="var(--fi-blue)"/>
    </g>
    <!-- PL -->
    <g class="flag flag-pl">
      <rect x="1512" y="6" width="88" height="50" fill="var(--white)"/>
      <rect x="1512" y="56" width="88" height="49" fill="var(--pl-red)"/>
    </g>
    <!-- CZ -->
    <g class="flag flag-cz">
      <rect x="1603" y="6" width="97" height="50" fill="var(--white)"/>
      <rect x="1603" y="56" width="97" height="49" fill="var(--red)"/>
      <polygon points="1603,6 1652,55.5 1603,105" fill="var(--cz-blue)"/>
    </g>
    <!-- GR -->
    <g class="flag flag-gr">
      <rect x="1705" y="6" width="111" height="99" fill="var(--white)"/>
      <rect x="1705" y="6" width="111" height="11" fill="var(--gr-blue)"/>
      <rect x="1705" y="28" width="111" height="11" fill="var(--gr-blue)"/>
      <rect x="1705" y="50" width="111" height="11" fill="var(--gr-blue)"/>
      <rect x="1705" y="72" width="111" height="11" fill="var(--gr-blue)"/>
      <rect x="1705" y="94" width="111" height="11" fill="var(--gr-blue)"/>
      <rect x="1705" y="6" width="44" height="55" fill="var(--gr-blue)"/>
      <rect x="1722" y="6" width="10" height="55" fill="var(--white)"/>
      <rect x="1705" y="28" width="44" height="11" fill="var(--white)"/>
    </g>
    <!-- Bayern -->
    <rect class="flag flag-bavaria" x="1820" y="6" width="128" height="99" fill="url(#bavaria-tone)" role="img" aria-label="Bayerische Rautenflagge mit Staatswappen"/>
  </g>

  <g class="reflection" clip-path="url(#clip-reflection)">
    <use href="#flags" transform="translate(0,210) scale(1,-1)"/>
    <rect x="0" y="105" width="1955" height="35" fill="url(#fade)"/>
  </g>
</svg>
</body>
</html>
```